Save our Business Card - We need your help

We need a fresh look on our business cards. We like it as it is, but it's not quite getting the 'wow' effect that we desire.
We're a tech startup building a cloud based solution for retailers consisting of Point of Sale, Inventory management and CRM.
The design should communicate a sense of a company that cares about the little things, design and relationships.
You can have a look at our website www.tillnest.com to get a feel for what we're like. Please feel free to message us for any further clarification
Target Market(s)
Our Customers are retail busines owners, cafe owners, other startups etc.
Industry/Entity Type
Building
Colors
Designer to choose colors to be used in the design.
Look and feel
Each slider illustrates characteristics of the customer's brand and the style your logo design should communicate.

```html
<!DOCTYPE html>
<html lang="en">
<head>
<meta charset="utf-8">
<title>Tillnest Business Card</title>
<link rel="stylesheet" href="https://fonts.googleapis.com/css2?family=Ubuntu:wght@400;500;700&display=swap">
<style>
  :root {
    --stage: #ece9e4;
    --amber-deep: #e48a1c;
    --amber: #f0a722;
    --sun: #f6c62a;
    --paper: #ffffff;
    --ink: #3a3a3a;
    --ink-soft: #6b6b6b;
    --brand: #f29a1e;
  }
  * { box-sizing: border-box; margin: 0; padding: 0; }
  html, body { width: 1200px; height: 1000px; overflow: hidden; }
  body {
    background: var(--stage);
    font-family: "Ubuntu", sans-serif;
    position: relative;
  }
  .card {
    position: absolute;
    left: 250px;
    width: 700px;
    height: 400px;
    overflow: hidden;
    box-shadow: 0 6px 18px rgba(0,0,0,0.15);
  }
  .card-back {
    top: 60px;
    background: linear-gradient(120deg, var(--amber-deep) 0%, var(--sun) 45%, var(--amber) 100%);
    display: flex;
    align-items: center;
    justify-content: center;
  }
  .back-brand {
    display: flex;
    align-items: center;
    gap: 18px;
  }
  .back-brand .brand-square {
    width: 60px; height: 60px; background: var(--paper);
  }
  .back-brand .brand-name {
    color: var(--paper);
    font-size: 52px;
    font-weight: 500;
  }
  .card-front {
    top: 540px;
    background: var(--paper);
  }
  .front-wave { position: absolute; inset: 0; }
  .front-content {
    position: absolute;
    left: 48px;
    top: 36px;
    width: 420px;
  }
  .front-brand {
    display: flex;
    align-items: center;
    gap: 12px;
  }
  .front-brand .brand-square {
    width: 34px; height: 34px; background: var(--brand);
  }
  .front-brand .brand-name {
    color: var(--brand);
    font-size: 34px;
    font-weight: 700;
  }
  .name-ribbon {
    margin-top: 18px;
    margin-left: -48px;
    width: 270px;
    height: 38px;
    background: var(--amber);
    clip-path: polygon(0 0, 100% 0, 88% 100%, 0 100%);
    display: flex;
    align-items: center;
    padding-left: 62px;
    color: var(--paper);
    font-size: 21px;
    font-weight: 500;
  }
  .role {
    margin-top: 8px;
    margin-left: 14px;
    font-size: 16px;
    font-weight: 700;
    color: var(--ink);
  }
  .contact-list {
    list-style: none;
    margin-top: 22px;
    margin-left: 14px;
  }
  .contact-list li {
    display: flex;
    align-items: center;
    gap: 12px;
    height: 29px;
    font-size: 14px;
    color: var(--ink-soft);
  }
  .contact-list svg { width: 14px; height: 14px; fill: var(--ink-soft); flex: none; }
</style>
</head>
<body>

<section class="card card-back">
  <div class="back-brand">
    <span class="brand-square"></span>
    <span class="brand-name">Tillnest</span>
  </div>
</section>

<section class="card card-front">
  <svg class="front-wave" width="700" height="400" viewBox="0 0 700 400">
    <defs>
      <linearGradient id="waveFill" x1="0" y1="0" x2="1" y2="1">
        <stop offset="0" stop-color="#f6c62a"/>
        <stop offset="1" stop-color="#e8901d"/>
      </linearGradient>
    </defs>
    <path d="M440 0 C 600 90, 500 300, 590 400 L700 400 L700 0 Z" fill="url(#waveFill)"/>
  </svg>

  <div class="front-content">
    <div class="front-brand">
      <span class="brand-square"></span>
      <span class="brand-name">Tillnest</span>
    </div>
    <div class="name-ribbon">Mara Quint</div>
    <p class="role">Manager</p>

    <ul class="contact-list">
      <li>
        <svg viewBox="0 0 14 14"><path d="M7 0a5 5 0 0 0-5 5c0 4 5 9 5 9s5-5 5-9a5 5 0 0 0-5-5zm0 7a2 2 0 1 1 0-4 2 2 0 0 1 0 4z"/></svg>
        Address: C-Wing, KL Court, Ohio 4410
      </li>
      <li>
        <svg viewBox="0 0 14 14"><path d="M4 0h6a1 1 0 0 1 1 1v12a1 1 0 0 1-1 1H4a1 1 0 0 1-1-1V1a1 1 0 0 1 1-1zm0 2v9h6V2z"/></svg>
        Mobile: +1234509876
      </li>
      <li>
        <svg viewBox="0 0 14 14"><path d="M3 0l3 3-2 2c1 2 3 4 5 5l2-2 3 3-2 3C6 14 0 8 0 3z"/></svg>
        Phone: +1234509876
      </li>
      <li>
        <svg viewBox="0 0 14 14"><path d="M0 2h14v10H0zM1 3l6 5 6-5v-.5H1z"/></svg>
        Email: hello@tillnest.com
      </li>
      <li>
        <svg viewBox="0 0 14 14"><path d="M7 0a7 7 0 1 0 0 14A7 7 0 0 0 7 0zm0 1.5c.9 1 1.5 2.9 1.6 4.8H5.4C5.5 4.4 6.1 2.5 7 1.5zM1.6 7.7h2.4c.1 1.7.5 3.2 1.1 4.3A5.6 5.6 0 0 1 1.6 7.7zm0-1.4A5.6 5.6 0 0 1 5.1 2C4.5 3.1 4.1 4.6 4 6.3zm5.4 6.2c-.9-1-1.5-2.9-1.6-4.8h3.2c-.1 1.9-.7 3.8-1.6 4.8zM8.9 12c.6-1.1 1-2.6 1.1-4.3h2.4a5.6 5.6 0 0 1-3.5 4.3zM10 6.3c-.1-1.7-.5-3.2-1.1-4.3a5.6 5.6 0 0 1 3.5 4.3z"/></svg>
        Website: www.tillnest.com
      </li>
    </ul>
  </div>
</section>

</body>
</html>
```